Talvor GmbH business card

We Talvor GmbH based in Switzerland are looking for a business card design. The Fresh Jung, appealing to customers of all kinds. We already have a logo to upload but still a business card. Details: Talvor GmbH Address: Lindenweg 14b in 9476 Brugwil. Tel: 41 79 462 37 18, web: Talvor.ch, E-mail: info@Talvor.ch Facebook: Talvor GmbH. I am the Managing Director: Luka Petrovac. On reverse: Title: Transporter and bus rental Gross: Without deposit Super prices
Contact Information for Business Card
Siehe Projektbeschreibung
Requirements
Should not have
- Other pictures

```html
<!DOCTYPE html>
<html lang="de">
<head>
<meta charset="utf-8">
<title>Talvor GmbH – Visitenkarte</title>
<link rel="stylesheet" href="https://fonts.googleapis.com/css2?family=Arimo:wght@400;700&display=swap">
<style>
  :root {
    --navy: #1b1c7c;
    --steel: #7f95b8;
    --steel-dark: #5a6da5;
    --muted: #66799c;
    --paper: #ffffff;
    --backdrop: #ececec;
  }
  * { margin: 0; padding: 0; box-sizing: border-box; }
  html, body { width: 1093px; height: 1200px; overflow: hidden; }
  body {
    background: var(--backdrop);
    font-family: "Arimo", Arial, sans-serif;
    position: relative;
  }
  .card {
    position: absolute;
    width: 833px;
    height: 483px;
    background: var(--paper);
    overflow: hidden;
  }
  .card-front { left: 135px; top: 106px; }
  .card-back  { left: 129px; top: 637px; }
  .card-art { position: absolute; inset: 0; }

  .brand-name {
    position: absolute;
    color: var(--navy);
    font-weight: 700;
    white-space: nowrap;
    line-height: 1;
  }
  .front-brand { left: 86px; top: 66px; font-size: 42px; letter-spacing: 1px; }
  .panel-brand { left: 612px; top: 249px; font-size: 36px; }
  .back-brand  { left: 62px; top: 218px; font-size: 54px; letter-spacing: 1px; }

  .service {
    position: absolute;
    left: 86px;
    color: var(--navy);
    line-height: 1;
    white-space: nowrap;
  }
  .service-large { font-size: 31px; }
  .service-small { font-size: 21px; }

  .benefits { position: absolute; left: 208px; top: 334px; list-style: none; }
  .benefit {
    display: flex;
    align-items: center;
    gap: 12px;
    color: var(--steel);
    font-size: 31px;
    height: 49px;
    white-space: nowrap;
  }
  .benefit svg { width: 28px; height: 30px; flex: none; }

  .person { position: absolute; right: 76px; top: 82px; text-align: right; }
  .person-name { color: var(--navy); font-weight: 700; font-size: 24px; letter-spacing: 0.5px; }
  .person-role { color: var(--muted); font-size: 22px; margin-top: 16px; }

  .contact-list { position: absolute; right: 112px; top: 193px; list-style: none; text-align: right; }
  .contact-item {
    height: 45.4px;
    display: flex;
    align-items: center;
    justify-content: flex-end;
    color: var(--navy);
    font-size: 23px;
    white-space: nowrap;
  }
</style>
</head>
<body>

<section class="card card-front" aria-label="Vorderseite">
  <svg class="card-art" viewBox="0 0 833 483" aria-hidden="true">
    <defs>
      <linearGradient id="steelFadeFront" x1="0" y1="0" x2="0" y2="1">
        <stop offset="0" stop-color="#8ea2c0"/>
        <stop offset="0.45" stop-color="#f4f6fa"/>
        <stop offset="0.62" stop-color="#ffffff"/>
        <stop offset="1" stop-color="#8a9fbd"/>
      </linearGradient>
    </defs>
    <polygon points="649,0 833,0 833,483 649,483 493,234" fill="url(#steelFadeFront)"/>
    <polyline points="636,0 474,234 642,483" fill="none" stroke="var(--steel)" stroke-width="6"/>
  </svg>

  <div class="brand-name front-brand">Talvor</div>

  <p class="service service-large" style="top:161px">TRANSPORTER</p>
  <p class="service service-small" style="top:205px">UND</p>
  <p class="service service-large" style="top:242px">BUS VERMIETUNG</p>

  <ul class="benefits">
    <li class="benefit">
      <svg viewBox="0 0 28 30"><path d="M2 6 L11 28 L26 2" fill="none" stroke="var(--steel)" stroke-width="4"/></svg>
      OHNE KAUTION
    </li>
    <li class="benefit">
      <svg viewBox="0 0 28 30"><path d="M2 6 L11 28 L26 2" fill="none" stroke="var(--steel)" stroke-width="4"/></svg>
      SUPER PREISE
    </li>
  </ul>

  <div class="brand-name panel-brand">Talvor</div>
</section>

<section class="card card-back" aria-label="Rückseite">
  <svg class="card-art" viewBox="0 0 833 483" aria-hidden="true">
    <defs>
      <linearGradient id="steelFadeBack" x1="0" y1="0" x2="0" y2="1">
        <stop offset="0" stop-color="#8ea2c0"/>
        <stop offset="0.45" stop-color="#f4f6fa"/>
        <stop offset="0.62" stop-color="#ffffff"/>
        <stop offset="1" stop-color="#8a9fbd"/>
      </linearGradient>
    </defs>
    <polygon points="0,0 220,0 404,235 211,483 0,483" fill="url(#steelFadeBack)"/>
    <polyline points="231,0 418,235 221,483" fill="none" stroke="var(--steel)" stroke-width="6"/>

    <g class="contact-bands">
      <rect x="760" y="193" width="73" height="45" fill="var(--steel)"/>
      <rect x="760" y="238" width="73" height="46" fill="var(--steel-dark)"/>
      <rect x="760" y="284" width="73" height="45" fill="var(--steel)"/>
      <rect x="760" y="329" width="73" height="46" fill="var(--steel-dark)"/>
      <rect x="760" y="375" width="73" height="45" fill="var(--steel)"/>
    </g>

    <g class="contact-icons" stroke="#fff" stroke-width="2.5">
      <g transform="translate(745,216)">
        <polygon points="0,-24 24,0 0,24 -24,0" fill="#4b5b98"/>
        <path d="M-5,-9 l4,0 l2,5 l-3,2 q2,5 7,7 l2,-3 l5,2 l0,4 q-1,3 -5,2 q-12,-4 -15,-15 q0,-4 3,-4z" fill="#fff" stroke="none"/>
      </g>
      <g transform="translate(745,261)">
        <polygon points="0,-24 24,0 0,24 -24,0" fill="#6f83ae"/>
        <rect x="-10" y="-7" width="20" height="14" fill="none" stroke-width="2"/>
        <path d="M-10,-7 L0,2 L10,-7" fill="none" stroke-width="2"/>
      </g>
      <g transform="translate(745,306)">
        <polygon points="0,-24 24,0 0,24 -24,0" fill="#4b5b98"/>
        <circle r="10" fill="none" stroke-width="2"/>
        <ellipse rx="4.5" ry="10" fill="none" stroke-width="1.6"/>
        <path d="M-10,0 H10 M-8,-5 H8 M-8,5 H8" fill="none" stroke-width="1.6"/>
      </g>
      <g transform="translate(745,352)">
        <polygon points="0,-24 24,0 0,24 -24,0" fill="#6f83ae"/>
        <circle r="8" fill="#fff" stroke="none"/>
      </g>
      <g transform="translate(745,397)">
        <polygon points="0,-24 24,0 0,24 -24,0" fill="#4b5b98"/>
        <path d="M0,11 C-4,5 -8,1 -8,-3 A8,8 0 0 1 8,-3 C8,1 4,5 0,11z" fill="#fff" stroke="none"/>
        <circle cy="-3" r="3" fill="#4b5b98" stroke="none"/>
      </g>
    </g>
  </svg>

  <div class="brand-name back-brand">Talvor</div>

  <div class="person">
    <p class="person-name">LUKA PETROVAC</p>
    <p class="person-role">Geschäftsführer</p>
  </div>

  <ul class="contact-list">
    <li class="contact-item">+41 79 462 37 18</li>
    <li class="contact-item">info@Talvor.ch</li>
    <li class="contact-item">www.Talvor.ch</li>
    <li class="contact-item">Talvor GmbH</li>
    <li class="contact-item">Lindenweg 14b in 9476 Brugwil</li>
  </ul>
</section>

</body>
</html>
```